Corvelle Matchmaking - Innovative AI-based Online Dating App

Hello, I am creating a new online dating app that subsumes the personalization and compatibility analysis of human matchmaking, but is combined with the convenience of modern dating apps such as brisket. The app is called Corvelle.

There is a lot of pain and fatigue in modern online dating. Corvelle uses a concise but effective questionnaire that is combined with cutting-edge AI, social psychology research, and psycholinguistic modelling to effectively and conveniently find dating matches with real compatibility - as opposed to any major app on the market. A personalized introduction for every user is generated everyday to introduce you to a new potential match - this introduction is totally unique and will never be seen before or again. The introduction is intertwined with the user’s images to create an attractive “newsletter” feel.

"Corvelle" is Italian for lagoon, which is "a shallow body of water protected from a larger body of water (usually the ocean) by sandbars, barrier islands, or coral reefs." Lagoons are beautiful, tropical, lush watery paradises - as I see it. This is meant to be the inspiration for the feel, color scheme and design of the app.

To that end, I have included concept images of lagoons to evoke the feeling of a paradise getaway where one may meet their soulmate. This is the feeling I would like to convey with the minimalist app design this product needs to compete.

I have included screenshots of the current app UI. There is a screen for
1) potential matches and incoming likes (just like Brisket) with a logo at the top. There are “Like”, “Dislike”, “Super Like”, and “Super Dislike” buttons that float over the screen as it scrolls. These button shape/colors likely need to change to match the rest of the design
2) Overview of message threads with each match
3) View of message threads
4) Settings page

I would like
1) the logo/header image to be redone (as well as the like/dislike/super like/super dislike buttons to be redone to match the new design)
2) icons for the 4 pages in the bottom navigation bar to be redone
3) color scheme to be optimized and evoking of the desired paradise but professional feeling of a hyper-intelligent (but also empathetic) matchmaker
4) design for the settings screen (to look professional and competitive with other dating apps)

The color scheme /layout/spacing/font(s) for the bubbles on the screen where new potential matches are introduced is the most important part of the design I’m looking for. It’s currently a stack of rounded rectangles basically, but I’m open to all ideas to make this app look as professional as possible while conveying the desired elegance, empathy, and uniqueness of the brand.

Thank you!

Target Market(s)

Single men and women ages 20 - 45

Industry/Entity Type

Online dating / Matchmaking

Requirements
Must have
• For the main screen where new users are being introduced (i.e. the "swipe" page on most dating apps) - some amount of matchmaking introductory text MUST be shown above the user's first profile picture, as indicated in the current screenshots.
Nice to have
• Re-designs of the top "Corvelle" logo/emblem would be nice. If changing the logo, some emblem or graphic in addition to just the text of "Corvelle" would be nice. (Like the way "plumway" has its red flame emblem)
Should not have
• The main "swipe" page should not look identical to other dating apps in the sense of being >90% just a user's first dating profile image. The competitive edge to this app is the user-to-user specific matchmaking introductory text, so some of that must be visible before a user scrolls down for further profile information.

```html
<!DOCTYPE html>
<html lang="en">
<head>
<meta charset="utf-8">
<title>Corvelle app screens</title>
<link href="https://fonts.googleapis.com/css2?family=Nunito:wght@400;500;600;700;800&display=swap" rel="stylesheet">
<style>
:root{
  --bg:#e3e9f1;
  --teal:#00bfbd;
  --teal-soft:#c9f5f2;
  --teal-tint:#effdfd;
  --ink:#1f2a33;
  --muted:#6b7580;
  --panel:#f3f5f8;
  --line:#dde2e8;
  --white:#ffffff;
  --blue:#2f7ef0;
  --orange:#f08a24;
  --red:#ef3e46;
}
*{box-sizing:border-box;margin:0;padding:0}
html,body{width:1200px;height:524px;overflow:hidden}
body{background:var(--bg);font-family:"Nunito",sans-serif;color:var(--ink);position:relative}
.screen{position:absolute;top:50px;width:195px;height:422px;border-radius:20px;background:var(--white);overflow:hidden}
.screen--teal{background:var(--teal)}
.abs{position:absolute}
.status{position:absolute;top:8px;left:18px;right:16px;height:10px;display:flex;justify-content:space-between;align-items:center;font-size:7.5px;font-weight:600}
.status svg{width:32px;height:8px}
.home-bar{position:absolute;bottom:5px;left:63px;width:70px;height:2px;border-radius:2px;background:var(--ink)}
.screen--teal .home-bar{background:var(--white)}
.brand{position:absolute;display:flex;align-items:center;gap:3px;color:var(--teal);font-weight:800;font-size:13.5px;letter-spacing:-.2px}
.brand-mark{width:11px;height:11px;border-radius:3px;background:var(--teal)}
/* login */
.brand--hero{left:0;right:0;top:82px;justify-content:center;color:var(--white);font-size:29px;gap:8px}
.brand--hero .brand-mark{width:27px;height:27px;border-radius:6px;background:var(--white)}
.login-card{position:absolute;left:8px;top:131px;width:179px;height:208px;border-radius:12px;background:var(--white)}
.field{position:absolute;left:18px;width:159px;height:22px;border-radius:11px;background:var(--panel);font-size:7px;color:var(--muted);padding:0 8px;display:flex;align-items:center;justify-content:space-between}
.forgot{position:absolute;right:18px;top:196px;font-size:7px;color:var(--muted)}
.btn-primary{position:absolute;left:18px;top:213px;width:159px;height:22px;border-radius:11px;background:var(--teal);color:var(--white);font-size:7.5px;font-weight:600;display:flex;align-items:center;justify-content:center}
.divider-or{position:absolute;left:18px;top:252px;width:159px;height:8px;font-size:6.5px;color:var(--muted);display:flex;align-items:center;gap:8px}
.divider-or::before,.divider-or::after{content:"";flex:1;height:1px;background:var(--line)}
.btn-social{position:absolute;left:18px;width:159px;height:22px;border-radius:11px;border:1px solid var(--teal);background:var(--teal-tint);font-size:7px;display:flex;align-items:center;gap:7px;padding-left:6px}
.btn-social .dot{width:9px;height:9px;border-radius:50%}
/* intro */
.top-icons{position:absolute;right:8px;top:33px;display:flex;gap:9px}
.top-icons svg{width:11px;height:11px}
.intro{position:absolute;left:8px;top:61px;width:179px;height:106px;border-radius:10px;background:var(--teal-soft);padding:9px 8px;font-size:6.7px;line-height:9px;color:var(--ink)}
.intro b{font-weight:700}
.photo-card{position:absolute;left:8px;top:175px;width:179px;height:207px;border-radius:10px 10px 0 0;background:linear-gradient(160deg,#3f5634 0%,#25331f 45%,#4d3c2c 75%,#1c2218 100%)}
.photo-card .name{position:absolute;left:8px;top:137px;color:var(--white);font-size:12px;font-weight:600}
.action{position:absolute;border-radius:50%;background:rgba(120,135,145,.7);display:flex;align-items:center;justify-content:center}
.action svg{width:55%;height:55%}
.nav{position:absolute;left:0;right:0;top:382px;height:40px;background:var(--white);display:flex;justify-content:space-around;padding:6px 12px 0}
.nav svg{width:14px;height:14px}
/* profile */
.profile-card{position:absolute;left:8px;top:61px;width:179px;height:104px;border-radius:10px;background:var(--panel)}
.avatar{position:absolute;border-radius:50%}
.stat{position:absolute;top:67px;width:60px;text-align:center}
.stat strong{display:block;font-size:14.5px;font-weight:700}
.stat span{font-size:5.8px;color:var(--muted)}
.section-title{position:absolute;left:8px;font-size:8px;font-weight:600}
.settings{position:absolute;left:8px;width:179px;border-radius:10px;background:var(--panel)}
.row{position:absolute;left:8px;right:8px;display:flex;justify-content:space-between;font-size:6.7px;font-weight:600}
.row .val{font-weight:500;color:var(--muted)}
.track{position:absolute;left:8px;right:8px;height:1px;background:var(--line)}
.fill{position:absolute;height:1.5px;background:var(--teal);top:-.25px}
.knob{position:absolute;top:-6px;width:12px;height:12px;border-radius:50%;background:var(--white);box-shadow:0 1px 3px rgba(0,0,0,.2)}
.hr{position:absolute;left:8px;right:8px;height:1px;background:var(--line)}
.toggle{position:absolute;right:8px;top:39px;width:24px;height:13px;border-radius:7px;background:var(--teal)}
.toggle::after{content:"";position:absolute;right:1px;top:1px;width:11px;height:11px;border-radius:50%;background:var(--white)}
/* messages */
.match{position:absolute;top:80px;height:89px;border-radius:8px}
.match-name{position:absolute;top:172px;font-size:6.8px;width:75px;text-align:center}
.thread{position:absolute;left:8px;right:8px;height:30px}
.thread .avatar{left:0;top:0;width:30px;height:30px}
.thread .online{position:absolute;left:23px;top:1px;width:7px;height:7px;border-radius:50%;background:var(--teal);border:1px solid var(--white)}
.thread .who{position:absolute;left:36px;top:6px;font-size:7px;font-weight:700}
.thread .msg{position:absolute;left:36px;top:17px;font-size:7px}
.thread .when{position:absolute;right:0;top:6px;font-size:5.8px;color:var(--muted)}
/* chat */
.chat-head{position:absolute;left:10px;top:30px;display:flex;align-items:center;gap:7px;font-size:7px;font-weight:600}
.chat-body{position:absolute;left:0;right:0;top:54px;height:328px;background:var(--panel)}
.chat-note{position:absolute;left:0;right:0;top:8px;text-align:center;font-size:6.8px}
.bubble{position:absolute;height:17px;border-radius:9px;padding:0 6px;display:flex;align-items:center;font-size:7px}
.bubble--out{right:8px;background:#dde1e7}
.bubble--in{left:30px;background:var(--teal);color:var(--ink)}
.composer{position:absolute;left:8px;top:390px;width:179px;height:20px;border-radius:10px;background:var(--panel);font-size:6.8px;color:var(--muted);display:flex;align-items:center;padding-left:8px}
.send{position:absolute;right:2px;top:2px;width:16px;height:16px;border-radius:50%;background:var(--teal);display:flex;align-items:center;justify-content:center}
</style>
</head>
<body>
<svg width="0" height="0" style="position:absolute">
  <defs>
    <symbol id="i-status" viewBox="0 0 32 8">
      <rect x="0" y="5" width="1.5" height="3" rx=".4" fill="currentColor"/><rect x="2.5" y="3.5" width="1.5" height="4.5" rx=".4" fill="currentColor"/><rect x="5" y="2" width="1.5" height="6" rx=".4" fill="currentColor"/><rect x="7.5" y="0" width="1.5" height="8" rx=".4" fill="currentColor"/>
      <path d="M12 3 Q15.5 0 19 3 M13.3 4.5 Q15.5 2.6 17.7 4.5" stroke="currentColor" stroke-width="1.1" fill="none"/><circle cx="15.5" cy="6.5" r="1" fill="currentColor"/>
      <rect x="21.5" y="1.2" width="9" height="5.5" rx="1.2" fill="currentColor"/><rect x="31" y="3" width="1" height="2" fill="currentColor"/>
    </symbol>
    <symbol id="i-grid" viewBox="0 0 24 24"><g fill="none" stroke="currentColor" stroke-width="1.6"><rect x="3" y="3" width="7.5" height="7.5" rx="1.5"/><rect x="13.5" y="3" width="7.5" height="7.5" rx="1.5"/><rect x="3" y="13.5" width="7.5" height="7.5" rx="1.5"/><rect x="13.5" y="13.5" width="7.5" height="7.5" rx="1.5"/></g></symbol>
    <symbol id="i-heart" viewBox="0 0 24 24"><path d="M12 20.5 C5 15.5 2.5 12.3 2.5 8.6 A4.9 4.9 0 0 1 12 6.6 A4.9 4.9 0 0 1 21.5 8.6 C21.5 12.3 19 15.5 12 20.5Z"/></symbol>
    <symbol id="i-chat" viewBox="0 0 24 24"><path d="M4 3.5h16a1.5 1.5 0 0 1 1.5 1.5v12a1.5 1.5 0 0 1-1.5 1.5h-5l-3 3-3-3H4A1.5 1.5 0 0 1 2.5 17V5A1.5 1.5 0 0 1 4 3.5Z"/><path class="inner" d="M12 14.5c-3-2-4.3-3.4-4.3-5a2.1 2.1 0 0 1 4.3-.6 2.1 2.1 0 0 1 4.3.6c0 1.6-1.3 3-4.3 5Z"/></symbol>
    <symbol id="i-gear" viewBox="0 0 24 24"><circle cx="12" cy="12" r="7" fill="none" stroke="currentColor" stroke-width="4" stroke-dasharray="3.1 2.4"/><circle cx="12" cy="12" r="6.2"/><circle class="inner" cx="12" cy="12" r="2.6"/></symbol>
  </defs>
</svg>

<!-- Sign in -->
<section class="screen screen--teal" style="left:50px">
  <div class="status" style="color:var(--white)"><span>9:41</span><svg><use href="#i-status"/></svg></div>
  <div class="brand brand--hero"><span class="brand-mark"></span>corvelle</div>
  <div class="login-card"></div>
  <div class="field" style="top:141px">Email or phone</div>
  <div class="field" style="top:167px">Password
    <svg width="11" height="11" viewBox="0 0 24 24" fill="none" stroke="#55606b" stroke-width="1.8"><path d="M2 12s4-6.5 10-6.5S22 12 22 12s-4 6.5-10 6.5S2 12 2 12Z"/><circle cx="12" cy="12" r="3"/><path d="M4 4l16 16"/></svg>
  </div>
  <div class="forgot">Forgot password?</div>
  <div class="btn-primary">Login</div>
  <div class="divider-or">or</div>
  <div class="btn-social" style="top:276px"><span class="dot" style="background:#e7493c"></span>Continue with Qivo</div>
  <div class="btn-social" style="top:306px"><span class="dot" style="background:var(--blue)"></span>Continue with Lumora</div>
  <div class="home-bar"></div>
</section>

<!-- Daily introduction -->
<section class="screen" style="left:275px">
  <div class="status"><span>9:41</span><svg><use href="#i-status"/></svg></div>
  <div class="brand" style="left:8px;top:31px"><span class="brand-mark"></span>corvelle</div>
  <div class="top-icons">
    <svg viewBox="0 0 24 24" fill="none" stroke="var(--ink)" stroke-width="1.8"><path d="M6 16V11a6 6 0 0 1 12 0v5l2 2H4Z"/><path d="M10 20.5a2 2 0 0 0 4 0"/></svg>
    <svg viewBox="0 0 24 24" fill="none" stroke="var(--ink)" stroke-width="1.8"><path d="M3 8h10M18 8h3M3 16h3M11 16h10"/><circle cx="15.5" cy="8" r="2.5"/><circle cx="8.5" cy="16" r="2.5"/></svg>
  </div>
  <article class="intro">Dear Brandon,<br>Allow me to introduce you <b>Natasha</b>, a captivating woman who possesses an enchanting blend of qualities that perfectly align with what you seek in a partner. Her shared interest in creativity is just the beginning of the profound connection you could share. Natsha's passion for games, documentaries, music and&nbsp; writing mirrors your own, promising endless hours of intellectual simulation and shared experiences.</article>
  <div class="photo-card" role="img" aria-label="Profile photo of Natasha in a knit hat and fleece coat, night city lights">
    <div class="name">Natasha, 24</div>
  </div>
  <div class="action" style="left:16px;top:339px;width:28px;height:28px"><svg viewBox="0 0 24 24" fill="var(--orange)"><path d="M4 4h3v10H4zM9 4h8.5a2 2 0 0 1 2 1.7l1 6.3a2 2 0 0 1-2 2.3H14l1 4a2 2 0 0 1-3.7 1.4L9 14Z"/></svg></div>
  <div class="action" style="left:53px;top:333px;width:40px;height:40px"><svg viewBox="0 0 24 24" stroke="var(--red)" stroke-width="3" stroke-linecap="round"><path d="M6 6l12 12M18 6L6 18"/></svg></div>
  <div class="action" style="left:101px;top:333px;width:40px;height:40px"><svg viewBox="0 0 24 24" fill="#2ee6e0"><use href="#i-heart"/></svg></div>
  <div class="action" style="left:150px;top:339px;width:28px;height:28px"><svg viewBox="0 0 24 24" fill="var(--blue)"><path d="M12 2.5l2.9 6 6.6.8-4.9 4.5 1.3 6.5L12 17l-5.9 3.3 1.3-6.5-4.9-4.5 6.6-.8Z"/></svg></div>
  <nav class="nav">
    <svg style="color:#8a949e"><use href="#i-grid"/></svg>
    <svg viewBox="0 0 24 24" fill="var(--teal)"><use href="#i-heart"/></svg>
    <svg viewBox="0 0 24 24" fill="none" stroke="#8a949e" stroke-width="1.6"><use href="#i-chat"/></svg>
    <svg viewBox="0 0 24 24" fill="var(--white)" style="color:#8a949e"><use href="#i-gear"/></svg>
  </nav>
  <div class="home-bar"></div>
</section>

<!-- Settings -->
<section class="screen" style="left:500px">
  <div class="status"><span>9:41</span><svg><use href="#i-status"/></svg></div>
  <div class="brand" style="left:8px;top:31px"><span class="brand-mark"></span>corvelle</div>
  <div class="profile-card">
    <div class="avatar" style="left:8px;top:8px;width:50px;height:50px;background:radial-gradient(circle at 50% 40%,#6b4a3a 0 28%,#1e8ee6 30%,#0a6fd0)" role="img" aria-label="Brandon's profile photo"></div>
    <div class="abs" style="left:27px;top:49px;width:12px;height:12px;border-radius:50%;background:var(--teal);border:1.5px solid var(--white)"></div>
    <div class="abs" style="left:66px;top:23px;font-size:9px;font-weight:600">Brandon</div>
    <div class="abs" style="left:66px;top:35px;font-size:5.8px;color:var(--muted);display:flex;align-items:center;gap:2px"><span style="width:7px;height:7px;border-radius:50%;background:var(--blue)"></span>Not verified</div>
    <div class="stat" style="left:14px"><strong>87</strong><span>Likes me</span></div>
    <div class="abs" style="left:89px;top:70px;width:1px;height:20px;background:var(--line)"></div>
    <div class="stat" style="left:104px"><strong>99+</strong><span>My Likes</span></div>
  </div>
  <div class="section-title" style="top:177px">Discovery Settings</div>
  <div class="settings" style="top:195px;height:130px">
    <div class="row" style="top:8px"><span>Distance</span><span class="val">5 km</span></div>
    <div class="track" style="top:25px"><div class="fill" style="left:0;width:20px"></div><div class="knob" style="left:14px"></div></div>
    <div class="row" style="top:44px"><span>Expand search area</span></div>
    <div class="toggle"></div>
    <div class="hr" style="top:62px"></div>
    <div class="row" style="top:71px"><span>Show Me</span><span class="val">Women &nbsp;›</span></div>
    <div class="hr" style="top:87px"></div>
    <div class="row" style="top:96px"><span>Age</span><span class="val">22-27</span></div>
    <div class="track" style="top:113px"><div class="fill" style="left:9px;width:41px"></div><div class="knob" style="left:3px"></div><div class="knob" style="left:44px"></div></div>
  </div>
  <div class="section-title" style="top:337px">App Settings</div>
  <div class="settings" style="top:355px;height:40px">
    <div class="row" style="top:10px"><span>Privacy Policy</span><span class="val" style="color:var(--ink);font-size:9px;line-height:7px">›</span></div>
  </div>
  <nav class="nav">
    <svg style="color:#8a949e"><use href="#i-grid"/></svg>
    <svg viewBox="0 0 24 24" fill="none" stroke="#8a949e" stroke-width="1.6"><use href="#i-heart"/></svg>
    <svg viewBox="0 0 24 24" fill="none" stroke="#8a949e" stroke-width="1.6"><use href="#i-chat"/></svg>
    <svg viewBox="0 0 24 24" fill="var(--teal)" style="color:var(--teal)"><use href="#i-gear"/></svg>
  </nav>
  <div class="home-bar"></div>
</section>

<!-- Matches and messages -->
<section class="screen" style="left:725px">
  <div class="status"><span>9:41</span><svg><use href="#i-status"/></svg></div>
  <div class="brand" style="left:0;right:0;top:31px;justify-content:center"><span class="brand-mark"></span>corvelle</div>
  <div class="section-title" style="top:62px">New Matches</div>
  <div class="match" style="left:8px;width:75px;background:linear-gradient(160deg,#d9cdbd,#8b6a52 60%,#3a2a22)" role="img" aria-label="Photo of Alexa"></div>
  <div class="match" style="left:89px;width:75px;background:linear-gradient(160deg,#4a4a22,#b27b4f 55%,#2a2a16)" role="img" aria-label="Photo of Vanessa"></div>
  <div class="match" style="left:170px;width:40px;background:linear-gradient(160deg,#8c8f92,#3b3d40)" role="img" aria-label="Photo of another new match"></div>
  <div class="match-name" style="left:8px">Alexa</div>
  <div class="match-name" style="left:89px">Vanessa</div>
  <div class="section-title" style="top:193px">Messages</div>
  <div class="thread" style="top:210px">
    <div class="avatar" style="background:linear-gradient(150deg,#c89a72,#5a3a28)" role="img" aria-label="Abbie's photo"></div><span class="online"></span>
    <span class="who">Abbie</span><span class="msg">Hello, Brandon!</span><span class="when">Just Now</span>
  </div>
  <div class="thread" style="top:246px">
    <div class="avatar" style="background:linear-gradient(150deg,#b8c4cc,#5e6a72)" role="img" aria-label="Sienna's photo"></div><span class="online"></span>
    <span class="who">Sienna</span><span class="msg">How's your day, Brandon?</span><span class="when">08:34 AM</span>
  </div>
  <div class="thread" style="top:282px">
    <div class="avatar" style="background:linear-gradient(150deg,#6f9a7c,#2f4a3c)" role="img" aria-label="Erica's photo"></div>
    <span class="who">Erica</span><span class="msg" style="color:var(--muted)">I really love cats</span><span class="when">Yesteday</span>
  </div>
  <nav class="nav">
    <svg style="color:#8a949e"><use href="#i-grid"/></svg>
    <svg viewBox="0 0 24 24" fill="none" stroke="#8a949e" stroke-width="1.6"><use href="#i-heart"/></svg>
    <svg viewBox="0 0 24 24" fill="var(--teal)" stroke="var(--teal)" stroke-width="1.6"><use href="#i-chat"/><style>.nav .inner{fill:var(--white);stroke:none}</style></svg>
    <svg viewBox="0 0 24 24" fill="var(--white)" style="color:#8a949e"><use href="#i-gear"/></svg>
  </nav>
  <div class="home-bar"></div>
</section>

<!-- Conversation -->
<section class="screen" style="left:950px">
  <div class="status"><span>9:41</span><svg><use href="#i-status"/></svg></div>
  <div class="chat-head">
    <svg width="8" height="8" viewBox="0 0 24 24" fill="none" stroke="var(--ink)" stroke-width="3"><path d="M15 4l-8 8 8 8"/></svg>
    <span class="avatar" style="position:static;width:16px;height:16px;background:linear-gradient(150deg,#c89a72,#5a3a28)" role="img" aria-label="Abbie's photo"></span>Abbie
  </div>
  <div class="chat-body">
    <div class="chat-note">You matched with Abbie on 01/01/2024</div>
    <div class="bubble bubble--out" style="top:29px">Hello, Abbie!</div>
    <div class="avatar" style="left:8px;top:54px;width:16px;height:16px;background:linear-gradient(150deg,#c89a72,#5a3a28)" role="img" aria-label="Abbie's photo"></div>
    <div class="bubble bubble--in" style="top:54px">Hello, Brandon!</div>
    <svg class="abs" style="left:175px;top:57px" width="12" height="12" viewBox="0 0 24 24" fill="none" stroke="#55606b" stroke-width="1.8"><use href="#i-heart"/></svg>
    <div class="bubble bubble--out" style="top:79px">How's your day, Abbie?</div>
  </div>
  <div class="composer">Type a messages
    <span class="send"><svg width="9" height="9" viewBox="0 0 24 24" fill="none" stroke="var(--white)" stroke-width="2.2"><path d="M4 4l17 8-17 8 3-8Z M7 12h8"/></svg></span>
  </div>
  <div class="home-bar"></div>
</section>
</body>
</html>
```